Car Dealership needs Custom Graphics for new Website/Advertising

We would like 10 or so editable Graphics files for our new website but that we can also edit to use on Plazabook, Advertising etc.. I have uploaded our Logo and 2 Graphics we have found that we like the look of. One of the primary advertisements we want is to Buy Cars, hence the two examples. If you are using examples of cars, it is important a variety of car brands are represented i.e. do not just have Valdor or Marquesse cars. We would also like some templates that we could edit to highlight Car of the Week, Free Delivery and other services we offer. All Graphics should have a distinct theme that fits to each other and our website.

Our new website address is http://test2.larkwindow.co.uk/pinecrestautos2/ - this is currently under construction so will be changing daily. Please note the fonts, colors and design layout.

Our current/old website is www.pinecrestautos.net

Pinecrest Autos is a specialized car dealership selling vehicles to US Military personnel stationed overseas in Germany. Please bear this in mind when designing Graphics.

Please do not use Aunt Rowena in any of the designs - we are moving away from this in our new website.

Target Market(s)

US Military Personnel and Families stationed in Germany and Europe

Font styles to use
Sans Serif

Requirements
Must have
• Fresh, consistant design that works well with new website. Ads will be primarily featured in the carousel box on the home page of the site, so should scale apporpriately.
Should not have
• Aunt Rowena

```html
<!DOCTYPE html>
<html lang="en">
<head>
<meta charset="utf-8">
<title>Pinecrest Autos – We Want To Buy Your Car</title>
<link rel="stylesheet" href="https://fonts.googleapis.com/css2?family=Roboto+Condensed:wght@400;700;900&family=Audiowide&family=Share+Tech+Mono&display=swap">
<style>
  :root {
    --red: #e51b24;
    --red-deep: #b70f19;
    --navy: #123f5e;
    --navy-deep: #0b2a40;
    --black: #050505;
    --white: #ffffff;
    --ink: #151515;
    --shadow-grey: #8a8a8a;
    --photo-mist: #e9ecf1;
    --photo-sky: #c9d3de;
    --photo-warm: #c9a89a;
    --photo-road: #9aa0a8;
  }
  * { box-sizing: border-box; margin: 0; padding: 0; }
  html, body { width: 1200px; height: 830px; overflow: hidden; background: var(--white); }
  .banner {
    position: relative;
    width: 1200px;
    height: 830px;
    overflow: hidden;
    background: var(--white);
    font-family: "Roboto Condensed", sans-serif;
  }
  .hero-photo {
    position: absolute;
    left: 0; top: 0;
    width: 1200px; height: 700px;
    background: linear-gradient(100deg,
      var(--white) 0%,
      var(--white) 22%,
      var(--photo-mist) 42%,
      var(--photo-warm) 58%,
      var(--photo-sky) 72%,
      var(--photo-road) 100%);
  }
  .brand {
    position: absolute;
    left: 30px; top: 34px;
    display: flex;
    align-items: center;
    gap: 10px;
  }
  .brand-dot {
    width: 34px; height: 34px;
    border-radius: 50%;
    background: var(--ink);
  }
  .brand-text {
    display: flex;
    flex-direction: column;
    line-height: 1.1;
  }
  .brand-name {
    font-weight: 700;
    font-size: 22px;
    color: var(--ink);
  }
  .brand-tagline {
    font-size: 12px;
    letter-spacing: 1px;
    text-transform: uppercase;
    color: var(--ink);
  }
  .headline {
    position: absolute;
    left: 66px; top: 150px;
    font-weight: 900;
    font-size: 100px;
    line-height: 94px;
    color: var(--red);
    text-shadow: 5px 5px 0 var(--shadow-grey);
    letter-spacing: -1px;
  }
  .trade-ribbon {
    position: absolute;
    left: 64px; top: 400px;
    width: 720px; height: 70px;
  }
  .trade-ribbon svg { position: absolute; inset: 0; }
  .trade-ribbon-text {
    position: absolute;
    left: 30px; top: 0;
    height: 58px;
    display: flex;
    align-items: center;
    font-family: "Audiowide", sans-serif;
    font-size: 38px;
    letter-spacing: 2px;
    color: var(--white);
  }
  .services {
    position: absolute;
    left: 104px; top: 520px;
    width: 560px;
    display: flex;
    justify-content: space-between;
    font-family: "Share Tech Mono", monospace;
    font-size: 40px;
    letter-spacing: 8px;
    color: var(--ink);
  }
  .contact-bar {
    position: absolute;
    left: 0; top: 700px;
    width: 1200px; height: 130px;
  }
  .contact-bar-bg { position: absolute; inset: 0; }
  .phone-grid {
    position: absolute;
    left: 22px; top: 20px;
    display: grid;
    grid-template-columns: 22px repeat(3, auto);
    column-gap: 18px;
    row-gap: 24px;
    align-items: center;
    font-size: 25px;
    line-height: 30px;
    color: var(--white);
    white-space: nowrap;
  }
  .phone-grid svg { display: block; }
  .online-list {
    position: absolute;
    left: 700px; top: 14px;
    display: grid;
    grid-template-columns: 48px auto;
    row-gap: 14px;
    align-items: center;
    font-size: 36px;
    color: var(--white);
    white-space: nowrap;
  }
  .online-list svg { display: block; }
</style>
</head>
<body>
<main class="banner">
  <div class="hero-photo" role="img" aria-label="White sedan driving along a waterfront road with a blurred city skyline behind"></div>

  <header class="brand">
    <span class="brand-dot"></span>
    <span class="brand-text">
      <span class="brand-name">Pinecrest Autos</span>
      <span class="brand-tagline">Military Car Sales</span>
    </span>
  </header>

  <h1 class="headline">WE WANT TO BUY<br>YOUR CAR</h1>

  <div class="trade-ribbon">
    <svg width="720" height="70" viewBox="0 0 720 70">
      <defs>
        <linearGradient id="ribbonNavy" x1="0" y1="0" x2="0" y2="1">
          <stop offset="0" stop-color="#123f5e"/>
          <stop offset="1" stop-color="#0b2a40"/>
        </linearGradient>
      </defs>
      <polygon points="36,8 720,8 688,70 18,70" fill="var(--red)"/>
      <polygon points="24,0 700,0 672,58 0,58" fill="url(#ribbonNavy)"/>
    </svg>
    <span class="trade-ribbon-text">TRADE YOUR VEHICLE NOW</span>
  </div>

  <p class="services"><span>BUY</span><span>-</span><span>SELL</span><span>-</span><span>TRADE</span></p>

  <footer class="contact-bar">
    <svg class="contact-bar-bg" width="1200" height="130" viewBox="0 0 1200 130">
      <rect x="0" y="0" width="1200" height="130" fill="var(--red)"/>
      <polygon points="0,0 650,0 610,130 0,130" fill="var(--white)"/>
      <polygon points="0,0 642,0 602,130 0,130" fill="var(--black)"/>
    </svg>

    <div class="phone-grid">
      <svg width="18" height="28" viewBox="0 0 18 28"><path d="M12 2 C4 4 2 10 2 14 C2 18 4 24 12 26 L14 21 L10 19 C8 17 8 11 10 9 L14 7 Z" fill="var(--white)"/></svg>
      <span>09804417260</span><span>096418205934</span><span>096417352098</span>
      <svg width="18" height="30" viewBox="0 0 18 30"><rect x="2" y="2" width="14" height="26" rx="3" fill="none" stroke="var(--white)" stroke-width="2.5"/><rect x="6" y="23" width="6" height="2" fill="var(--white)"/></svg>
      <span>017690482315</span><span>015228703641</span><span>015229158306</span>
    </div>

    <div class="online-list">
      <svg width="30" height="22" viewBox="0 0 30 22"><rect x="1" y="1" width="28" height="20" fill="var(--white)"/><polyline points="2,2 15,13 28,2" fill="none" stroke="var(--red)" stroke-width="2.5"/><line x1="2" y1="20" x2="11" y2="11" stroke="var(--red)" stroke-width="2"/><line x1="28" y1="20" x2="19" y2="11" stroke="var(--red)" stroke-width="2"/></svg>
      <span>contact@pinecrestautos.net</span>
      <svg width="30" height="30" viewBox="0 0 30 30" fill="none" stroke="var(--white)" stroke-width="2"><circle cx="15" cy="15" r="13"/><ellipse cx="15" cy="15" rx="6" ry="13"/><line x1="2" y1="15" x2="28" y2="15"/><line x1="4" y1="8" x2="26" y2="8"/><line x1="4" y1="22" x2="26" y2="22"/><line x1="15" y1="2" x2="15" y2="28"/></svg>
      <span>www.pinecrestautos2</span>
    </div>
  </footer>
</main>
</body>
</html>
```